2 page PSD web design

I need a fairly simple website design built in PSD format for a site / blog in the finance niche. My current web address is www.spreadledgerhub.com. Yield Ledger Hub is a site that teaches people how to trade options with a focus on income strategies.

I need a simple homepage built and then another similar template for all other pages including blog posts.

The rough design layout is shown attached excel file. It is similar to www.marcusfelbring.com although I don't like the colors on his site at all. My logo is attached also, so the colours should be aligned with my logo.

In the header section, I will be giving away a free ebook called "Fluff-Free Manual for Calendar Wings" so I will need a 2D and 3D book cover designed as well. The design should be aligned with my logo and site design.

Industry/Entity Type

Finance

Requirements
Must have
• Everything is detailed in the excel file, but here is a list of must have items:

My current logo
ebook design and sign up section
under the ebook sign up section, need a big bold heading - "HELPING YOU TRADE IRON CONDORS AND OTHER INCOME STRATEGIES WITHOUT THE BS"
6 sidebar sections as detailed in excel file
Social Proof at top right, on the same line / level as the logo
"home advertise contact" in the top left in small discreet font
Should not have
• Do not want any photos or images on either of the pages

```html
<!DOCTYPE html>
<html lang="en">
<head>
<meta charset="utf-8">
<title>Yield Ledger Hub</title>
<link href="https://fonts.googleapis.com/css2?family=Open+Sans:wght@400;600;700;800&family=Oswald:wght@600;700&display=swap" rel="stylesheet">
<style>
:root{
  --page:#e9ebee;
  --white:#ffffff;
  --ink:#1f2a36;
  --muted:#6b7480;
  --blue:#1b5ea8;
  --blue-dark:#0f3f78;
  --blue-deep:#0a2f5c;
  --red:#c8322b;
  --line:#d8dce1;
  --soft:#f4f5f7;
  --footer:#dfe2e6;
}
*{box-sizing:border-box;margin:0;padding:0}
html,body{width:720px;height:1200px;overflow:hidden}
body{background:var(--page);font-family:"Open Sans",Arial,sans-serif;color:var(--ink);font-size:9px}
.page{width:660px;margin:0 auto;background:var(--white);height:1200px;position:relative}
.topbar{height:70px;display:flex;justify-content:space-between;align-items:flex-start;padding:8px 16px 0}
.util-links{display:flex;gap:10px;font-size:7px;text-transform:uppercase;color:var(--muted);letter-spacing:.5px}
.brand{display:flex;align-items:center;gap:7px;margin-top:10px}
.brand-square{width:22px;height:22px;background:var(--blue)}
.brand-name{font-size:19px;font-weight:800;color:var(--blue)}
.social-proof{text-align:right;margin-top:16px;font-size:11px;font-weight:700;color:var(--ink);line-height:1.35}
.social-proof span{display:block;font-weight:400;font-size:9px;color:var(--muted)}
.main-nav{height:30px;background:var(--blue);display:flex;align-items:center;padding:0 8px}
.main-nav a{color:var(--white);text-decoration:none;font-weight:700;font-size:9.5px;padding:0 11px;line-height:30px}
.main-nav a.active{background:var(--white);color:var(--blue)}
.hero{height:190px;background:linear-gradient(180deg,var(--blue-dark),var(--blue-deep));display:flex;align-items:center;padding:0 18px;gap:18px;color:var(--white)}
.hero-copy{width:200px;font-size:9.5px;line-height:1.5}
.hero-copy strong{display:block;font-size:10.5px;margin-bottom:8px}
.hero-copy p+p{margin-top:8px}
.ebook{width:150px;height:160px;background:linear-gradient(135deg,#d8382f,#9e1f1a);box-shadow:6px 6px 0 rgba(0,0,0,.25)}
.signup{flex:1;background:rgba(255,255,255,.08);padding:12px;border:1px solid rgba(255,255,255,.2)}
.signup h3{font-size:10px;font-weight:700;margin-bottom:8px}
.field{height:22px;background:var(--white);color:var(--muted);font-size:8px;padding:0 8px;line-height:22px;margin-bottom:7px}
.btn{display:block;background:var(--red);color:var(--white);text-align:center;font-weight:700;font-size:9.5px;line-height:24px;text-transform:uppercase}
.headline{height:90px;display:flex;align-items:center;justify-content:center;text-align:center;font-family:"Oswald",Arial,sans-serif;font-weight:700;font-size:25px;line-height:1.15;color:var(--ink);padding:0 40px;text-transform:uppercase}
.content{display:flex;gap:20px;padding:5px 16px 0}
.posts{width:418px}
.section-title{background:var(--soft);border-top:2px solid var(--blue);font-size:9px;font-weight:800;text-transform:uppercase;padding:7px 8px;margin-bottom:8px}
.post{display:flex;gap:10px;height:104px;border-bottom:1px solid var(--line);padding-bottom:8px;margin-bottom:9px}
.thumb{width:82px;height:82px;flex:none;background:#1c2d44}
.post-meta{font-size:7px;color:var(--muted)}
.post-title{font-size:11px;font-weight:700;color:var(--blue);margin:3px 0 4px}
.share{display:flex;gap:4px;margin-bottom:5px}
.share i{width:26px;height:9px;background:var(--line);display:block}
.excerpt{font-size:8px;line-height:1.5;color:var(--muted)}
.excerpt b{color:var(--red)}
.gap-top{margin-top:8px}
.sidebar{width:190px}
.widget{border:1px solid var(--line);padding:10px;margin-bottom:12px}
.widget h4{font-size:8px;font-weight:800;text-transform:uppercase;color:var(--blue)}
.widget .big{font-size:12px;font-weight:800;margin:3px 0}
.widget p{font-size:8px;line-height:1.45;color:var(--muted)}
.pill{display:inline-block;background:var(--blue);color:var(--white);font-size:7.5px;font-weight:700;padding:3px 8px;margin-top:5px}
.sponsor{height:30px;background:var(--soft);border:1px solid var(--line);margin-top:7px}
.ad{height:190px;background:var(--soft);border:1px solid var(--line);display:flex;align-items:center;justify-content:center;color:var(--muted);font-weight:700;font-size:9px;margin-bottom:12px}
.newsletter{background:var(--blue);color:var(--white);padding:12px}
.newsletter h4{font-size:9.5px;font-weight:800;text-transform:uppercase;line-height:1.35;margin-bottom:8px}
.newsletter .field{margin-bottom:6px}
.footer{position:absolute;left:0;right:0;bottom:0;height:62px;background:var(--footer);text-align:center;padding-top:16px}
.footer nav{display:flex;justify-content:center;gap:14px;font-size:8px;color:var(--ink)}
.footer p{font-size:7.5px;color:var(--muted);margin-top:8px}
</style>
</head>
<body>
<div class="page">
  <header class="topbar">
    <div>
      <nav class="util-links"><span>Home</span><span>Advertise</span><span>Contact</span></nav>
      <div class="brand"><div class="brand-square"></div><div class="brand-name">Yield Ledger Hub</div></div>
    </div>
    <div class="social-proof">Join a Community of 4279<span>Awesome Readers</span></div>
  </header>
  <nav class="main-nav">
    <a class="active">Articles &amp; Videos</a><a>Trading Philosophy</a><a>Learning Centre</a><a>Free Tools</a><a>Members Only</a><a>Work With Us</a><a>About</a>
  </nav>
  <section class="hero">
    <div class="hero-copy">
      <strong>Do You Want To Know The Truth About Iron Condors?</strong>
      <p>Learn How To Trade This Amazing Option Income Strategy With My FREE Ebook: Fluff-Free Manual for Calendar Wings.</p>
      <p>I will share with you my blueprint and all my tips and tricks for generating consistent monthly income with iron condors.</p>
    </div>
    <div class="ebook" role="img" aria-label="3D cover of the free ebook Fluff-Free Manual for Calendar Wings"></div>
    <form class="signup">
      <h3>Enter your details below</h3>
      <div class="field">Enter your first name...</div>
      <div class="field">Enter your email address</div>
      <span class="btn">Get Instant Access</span>
    </form>
  </section>
  <h1 class="headline">Helping you trade iron condors and others income strategies without the BS.</h1>
  <div class="content">
    <main class="posts">
      <div class="section-title">Latest Posts</div>
      <article class="post"><div class="thumb" role="img" aria-label="Follow Friday post graphic"></div><div><div class="post-meta">Posted by Dana Reel</div><div class="post-title">Top 10 Follow Friday Favorites and Top Influencers Week 42</div><div class="share"><i></i><i></i><i></i></div><p class="excerpt">I hope everyone had a great holiday and I'd like to wish you a happy New Year. I have a few changes coming in 2013 that I will be sharing with you soon, but for now I'll share my new plan for this post. <b>[Read More]</b></p></div></article>
      <article class="post"><div class="thumb" role="img" aria-label="Follow Friday post graphic"></div><div><div class="post-meta">Posted by Dana Reel</div><div class="post-title">Top 10 Follow Friday Favorites and Top Influencers Week 42</div><div class="share"><i></i><i></i><i></i></div><p class="excerpt">I hope everyone had a great holiday and I'd like to wish you a happy New Year. I have a few changes coming in 2013 that I will be sharing with you soon, but for now I'll share my new plan for this post. <b>[Read More]</b></p></div></article>
      <article class="post"><div class="thumb" role="img" aria-label="Follow Friday post graphic"></div><div><div class="post-meta">Posted by Dana Reel</div><div class="post-title">Top 10 Follow Friday Favorites and Top Influencers Week 42</div><div class="share"><i></i><i></i><i></i></div><p class="excerpt">I hope everyone had a great holiday and I'd like to wish you a happy New Year. I have a few changes coming in 2013 that I will be sharing with you soon, but for now I'll share my new plan for this post. <b>[Read More]</b></p></div></article>
      <div class="section-title gap-top">Featured Posts</div>
      <article class="post"><div class="thumb" role="img" aria-label="Follow Friday post graphic"></div><div><div class="post-meta">Posted by Dana Reel</div><div class="post-title">Top 10 Follow Friday Favorites and Top Influencers Week 42</div><div class="share"><i></i><i></i><i></i></div><p class="excerpt">I hope everyone had a great holiday and I'd like to wish you a happy New Year. I have a few changes coming in 2013 that I will be sharing with you soon, but for now I'll share my new plan for this post. <b>[Read More]</b></p></div></article>
      <article class="post"><div class="thumb" role="img" aria-label="Follow Friday post graphic"></div><div><div class="post-meta">Posted by Dana Reel</div><div class="post-title">Top 10 Follow Friday Favorites and Top Influencers Week 42</div><div class="share"><i></i><i></i><i></i></div><p class="excerpt">I hope everyone had a great holiday and I'd like to wish you a happy New Year. I have a few changes coming in 2013 that I will be sharing with you soon, but for now I'll share my new plan for this post. <b>[Read More]</b></p></div></article>
    </main>
    <aside class="sidebar">
      <div class="widget"><h4>Work With Us</h4><div class="big">ONE-ONE</div><p>We're ready to help you achieve the success you're looking for.</p><span class="pill">Get Connected &rsaquo;</span></div>
      <div class="widget"><h4>New to Options?</h4><p>Check out our comprehensive</p><div class="big">TRADING PROGRAM &rarr;</div></div>
      <div class="widget"><h4>Top Sponsors</h4><div class="sponsor"></div><div class="sponsor"></div><div class="sponsor"></div></div>
      <div class="ad">300 x 250</div>
      <div class="newsletter"><h4>Stay up to date with Yield Ledger Hub. New articles &amp; tutorials delivered straight to your inbox</h4><div class="field">Enter your email address</div><span class="btn">Let's Go</span></div>
    </aside>
  </div>
  <footer class="footer">
    <nav><span>Articles &amp; Videos</span><span>Trading Philosophy</span><span>Learning Centre</span><span>Free Tools</span><span>Members Only</span><span>Work With Us</span><span>About</span></nav>
    <p>&copy; 2010 - 2013 Yield Ledger Hub. All Rights Reserved.</p>
  </footer>
</div>
</body>
</html>
```